Torvenu Business Card Design Project

We need a business card design for torvenu.com a company based in Berlin, Germany.

?Torvenu is marketplace that enables people all over the world to monetize and exchange their individual knowledge and language skills through interactive video sessions. User are matched by their interests.

On Torvenu everybody can be student or teacher (seller or buyer).

We would love to see designs that use or main color blue and green. The design should communicate what Torvenu enables - see my notice above.

Looking so forward to your designs
Cheers from Berlin,
Konrad

Target Market(s)

globally

Industry/Entity Type

Teacher

Requirements
Must have
• Konrad Wielert
CEO
Torvenu.com

Torvenu e-Services GmbH
Lindgrubweg 27
10117 Berlin

Fon: +49 30 481 906 27 14
Mobile: 49 171 57 04 91 3
E-Mail: k.wielert@torvenu.com
Web: www.torvenu.com

```html
<!DOCTYPE html>
<html lang="en">
<head>
<meta charset="UTF-8">
<title>Torvenu Business Card</title>
<link href="https://fonts.googleapis.com/css2?family=Open+Sans:wght@400;600;700&display=swap" rel="stylesheet">
<style>
  :root {
    --backdrop: #2a2a2a;
    --paper: #ffffff;
    --brand-blue: #1b9ad6;
    --brand-green: #8cc63f;
    --brand-grey: #6d6e71;
    --stripe-grey: #a7a9ac;
    --ink: #4a4a4a;
  }
  * { margin: 0; padding: 0; box-sizing: border-box; }
  html, body {
    width: 1200px; height: 900px; overflow: hidden;
    background: var(--backdrop);
    font-family: "Open Sans", Arial, sans-serif;
  }
  .card-sheet {
    position: absolute; inset: 0;
    display: flex; align-items: center; justify-content: center; gap: 40px;
  }
  .card {
    position: relative;
    width: 540px; height: 310px;
    background: var(--paper);
    overflow: hidden;
    box-shadow: 0 10px 30px rgba(0,0,0,.45);
  }
  .card__wave { position: absolute; inset: 0; width: 100%; height: 100%; }

  .brand { position: absolute; display: flex; align-items: center; gap: 10px; }
  .brand__mark { width: 34px; height: 34px; background: var(--brand-blue); }
  .brand__name {
    font-weight: 400; font-size: 46px; line-height: 1;
    color: var(--brand-grey); letter-spacing: -1px;
  }

  .front .brand { left: 34px; top: 90px; }

  .person { position: absolute; left: 290px; top: 40px; }
  .person__name { font-size: 17px; font-weight: 700; color: var(--brand-blue); white-space: nowrap; }
  .person__role { font-size: 11px; font-weight: 600; color: var(--brand-green); margin-top: 2px; }

  .contact { position: absolute; left: 34px; top: 172px; list-style: none;
    font-size: 12.5px; line-height: 18px; color: var(--brand-blue); }
  .contact li { display: flex; align-items: center; gap: 8px; white-space: nowrap; }
  .contact .icon { width: 12px; height: 12px; flex: none; }
  .contact .blank { width: 12px; flex: none; }

  .front .web-vertical {
    position: absolute; left: 392px; top: 256px;
    font-size: 12px; color: var(--ink); white-space: nowrap;
    transform: rotate(-62deg); transform-origin: left top;
  }

  .back .brand { left: 92px; top: 122px; }
  .back .web { position: absolute; left: 136px; top: 168px;
    font-size: 13px; font-weight: 600; color: var(--brand-green); }
</style>
</head>
<body>
<main class="card-sheet">

  <section class="card front" aria-label="Business card front">
    <svg class="card__wave" viewBox="0 0 540 310" aria-hidden="true">
      <path d="M540,12 C452,12 420,96 378,172 C332,254 262,292 170,310" fill="none" stroke="var(--stripe-grey)" stroke-width="6"/>
      <path d="M540,26 C462,26 432,108 392,180 C344,262 272,298 188,310 L540,310 Z" fill="var(--brand-green)"/>
      <path d="M540,38 C472,38 444,118 404,188 C356,268 286,302 204,310 L540,310 Z" fill="var(--brand-blue)"/>
    </svg>

    <div class="brand">
      <span class="brand__mark"></span>
      <span class="brand__name">torvenu</span>
    </div>

    <div class="person">
      <p class="person__name">Konrad Wielert</p>
      <p class="person__role">CEO</p>
    </div>

    <ul class="contact">
      <li>
        <svg class="icon" viewBox="0 0 12 12"><path d="M6 1 L11 6 H9.5 V11 H7 V8 H5 V11 H2.5 V6 H1 Z" fill="var(--brand-green)"/></svg>
        Torvenu e-Services GmbH
      </li>
      <li><span class="blank"></span>Lindgrubweg 27</li>
      <li><span class="blank"></span>10117 Berlin</li>
      <li>
        <svg class="icon" viewBox="0 0 12 12"><path d="M2.5 1.5 L4.5 1.5 L5.2 4 L4 5 C4.6 6.5 5.5 7.4 7 8 L8 6.8 L10.5 7.5 L10.5 9.5 C6 10 2 6 2.5 1.5 Z" fill="var(--brand-green)"/></svg>
        +49 30 481 906 27 14
      </li>
      <li>
        <svg class="icon" viewBox="0 0 12 12"><rect x="3" y="1" width="6" height="10" rx="1" fill="none" stroke="var(--brand-green)" stroke-width="1.3"/></svg>
        49 171 57 04 91 3
      </li>
      <li>
        <svg class="icon" viewBox="0 0 12 12"><rect x="1" y="2.5" width="10" height="7" fill="var(--brand-green)"/><path d="M1 2.5 L6 6.5 L11 2.5" fill="none" stroke="#fff" stroke-width="1"/></svg>
        k.wielert@torvenu.com
      </li>
    </ul>

    <span class="web-vertical">www.torvenu.com</span>
  </section>

  <section class="card back" aria-label="Business card back">
    <svg class="card__wave" viewBox="0 0 540 310" aria-hidden="true">
      <path d="M540,8 C462,8 440,80 418,150 C392,236 350,288 290,310" fill="none" stroke="var(--stripe-grey)" stroke-width="6"/>
      <path d="M540,22 C474,22 454,92 432,160 C406,244 366,294 310,310 L540,310 Z" fill="var(--brand-green)"/>
      <path d="M540,34 C484,34 466,102 444,168 C418,250 380,298 328,310 L540,310 Z" fill="var(--brand-blue)"/>
    </svg>

    <div class="brand">
      <span class="brand__mark"></span>
      <span class="brand__name">torvenu</span>
    </div>
    <span class="web">www.torvenu.com</span>
  </section>

</main>
</body>
</html>
```